Kestrel Softball Tournaments Website Design

Our client would like us to design a website. The company is similar to Brightfield Sports USA (https://brightfieldsportsusa.example).

We prefer Adobe Fonts in the design. Lorem ipsum is fine to use for content, except for headers. Please keep track of any images used in your design. We plan on purchasing the images used.

Number of Pages Required

1 page

Font styles to use
Sans Serif

Colors
0054AA
0677BA
7BADD7
CADEEF
E8F1F8

```html
<!DOCTYPE html>
<html lang="en">
<head>
<meta charset="utf-8">
<title>Kestrel Softball Tournaments</title>
<link rel="stylesheet" href="https://fonts.googleapis.com/css2?family=Oswald:wght@500;600&family=Poppins:wght@400;500;600;700;800&display=swap">
<style>
:root{
  --navy:#0f1d3d;
  --blue:#2c4f8f;
  --hero-blue:#3a5a9c;
  --red:#e31e24;
  --submit:#e3341f;
  --yellow:#f5ec1a;
  --grey:#f5f5f5;
  --ink:#222;
  --white:#fff;
}
*{margin:0;padding:0;box-sizing:border-box}
html,body{width:1200px;height:3975px;overflow:hidden}
body{position:relative;font-family:'Poppins',sans-serif;color:var(--ink);background:var(--white)}
.abs{position:absolute}

/* hero */
.hero{left:0;top:0;width:1200px;height:655px;background:linear-gradient(120deg,#5d7bb5 0%,#3a5a9c 45%,#2a4684 100%)}
.hero-cut{left:0;top:600px;width:1200px;height:60px}
.brand{left:100px;top:36px;color:var(--white);font-weight:700;font-size:20px;line-height:24px;text-transform:uppercase;display:flex;align-items:center;gap:10px}
.brand .dot{width:18px;height:18px;border-radius:50%;background:var(--white)}
.menu{left:1058px;top:55px;width:40px}
.menu span{display:block;height:4px;background:var(--white);margin-bottom:7px;border-radius:2px}
.hero-kicker{left:0;width:1200px;top:212px;text-align:center;font-family:'Oswald',sans-serif;font-weight:600;font-size:56px;color:var(--white);line-height:64px}
.hero-title{left:0;width:1200px;top:258px;text-align:center;font-family:'Oswald',sans-serif;font-weight:600;font-size:120px;color:var(--white);line-height:130px;letter-spacing:-1px}
.hero-btn{left:481px;top:408px;width:238px;height:60px;border:2px solid var(--white);color:var(--white);font-size:26px;font-weight:500;display:flex;align-items:center;justify-content:center}
.arrow{top:296px;width:52px;height:52px}

/* section headings */
.sec-title{left:0;width:1200px;text-align:center;font-weight:800;font-size:44px;color:var(--blue);line-height:56px}
.rule{height:4px;background:var(--red)}

/* tournament rows */
.photo{width:463px;height:329px}
.row-title{font-weight:700;font-size:48px;color:var(--blue);line-height:60px;white-space:nowrap}
.row-copy{width:460px;font-size:15.5px;line-height:27px;font-weight:500;color:#333}
.pill{height:46px;border-radius:23px;background:var(--red);color:var(--white);font-size:15.5px;font-weight:600;display:flex;align-items:center;justify-content:center;width:160px}

/* about */
.about-bg{left:0;top:1930px;width:1200px;height:620px}
.about-copy{left:101px;top:2170px;width:440px;font-size:15.5px;line-height:25.7px;font-weight:600;color:#222}
.about-mark{left:610px;top:2230px;width:520px;text-align:center;color:var(--navy);font-weight:800;font-size:64px;line-height:76px;text-transform:uppercase;display:flex;flex-direction:column;align-items:center;gap:20px}
.about-mark .dot{width:60px;height:60px;border-radius:50%;background:var(--navy)}

/* steps */
.step{top:2702px;width:200px;text-align:center}
.step .badge{width:108px;height:108px;margin:0 auto;border-radius:50%;background:var(--yellow);border:3px solid var(--red);display:flex;align-items:center;justify-content:center}
.step h3{margin-top:14px;font-weight:700;font-size:23px;color:var(--blue);line-height:28px}
.step p{font-size:13.5px;color:var(--blue);line-height:20px}

/* contact */
.contact-bg{left:0;top:2920px;width:1200px;height:705px}
.contact-tag{left:511px;top:3026px;width:183px;height:40px;background:var(--white);border-radius:4px;color:var(--blue);font-size:20px;font-weight:500;display:flex;align-items:center;justify-content:center}
.field{background:var(--white);border-radius:4px;font-size:15px;color:#333;padding:14px 14px}
.submit{left:496px;top:3472px;width:208px;height:62px;border-radius:31px;background:var(--submit);color:var(--white);font-family:Georgia,serif;font-size:17px;display:flex;align-items:center;justify-content:center}

/* footer */
.foot-brand{left:0;width:1200px;top:3668px;text-align:center;color:var(--navy);font-weight:800;font-size:26px;line-height:32px;text-transform:uppercase}
.foot-nav{top:3824px;font-size:19px;color:#222;transform:translateX(-50%);white-space:nowrap}
.foot-line{left:99px;top:3898px;width:1002px;height:2px;background:#444}
.copyright{left:0;width:1200px;top:3922px;text-align:center;font-size:17px;color:#222}
</style>
</head>
<body>

<header>
  <div class="abs hero" role="img" aria-label="Softball fielder stretching to catch a ball, blue-tinted action photo"></div>
  <svg class="abs hero-cut" viewBox="0 0 1200 60" width="1200" height="60" aria-hidden="true">
    <polygon points="0,55 600,22 1200,55 1200,60 0,60" fill="#fff"/>
    <polygon points="600,22 1200,0 1200,54" fill="#0f1d3d"/>
  </svg>
  <div class="abs brand"><span class="dot"></span>Kestrel<br>Softball</div>
  <div class="abs menu"><span></span><span></span><span></span></div>
  <svg class="abs arrow" style="left:66px" viewBox="0 0 52 52" aria-hidden="true"><circle cx="26" cy="26" r="24" fill="none" stroke="#fff" stroke-width="2.5"/><polygon points="31,16 19,26 31,36" fill="none" stroke="#fff" stroke-width="2.5"/></svg>
  <svg class="abs arrow" style="left:1132px" viewBox="0 0 52 52" aria-hidden="true"><circle cx="26" cy="26" r="24" fill="none" stroke="#fff" stroke-width="2.5"/><polygon points="21,16 33,26 21,36" fill="none" stroke="#fff" stroke-width="2.5"/></svg>
  <h1>
    <span class="abs hero-kicker">KESTREL SOFTBALL</span>
    <span class="abs hero-title">TOURNAMENTS.</span>
  </h1>
  <div class="abs hero-btn">Learn More</div>
</header>

<main>
  <h2 class="abs sec-title" style="top:705px">SOFTBALL TOURNAMENTS</h2>
  <div class="abs rule" style="left:538px;top:769px;width:124px"></div>

  <div class="abs photo" style="left:99px;top:826px;background:linear-gradient(160deg,#8d8a80,#b98a60 45%,#c8946a)" role="img" aria-label="Batter swinging at a pitch on a dirt infield"></div>
  <h3 class="abs row-title" style="left:630px;top:870px">SPRING OPENER</h3>
  <p class="abs row-copy" style="left:633px;top:944px">Lorem ipsum dolor sit amet, consectetur adipiscing elit, sed do eiusmod tempor incididunt ut labore et dolore magna aliqua.</p>
  <div class="abs pill" style="left:633px;top:1048px">Read More</div>

  <h3 class="abs row-title" style="left:101px;top:1255px">SUMMER SERIES</h3>
  <p class="abs row-copy" style="left:101px;top:1330px">Lorem ipsum dolor sit amet, consectetur adipiscing elit, sed do eiusmod tempor incididunt ut labore et dolore magna aliqua.</p>
  <div class="abs pill" style="left:102px;top:1434px">Read More</div>
  <div class="abs photo" style="left:632px;top:1212px;background:linear-gradient(180deg,#3b79b8,#9fb3c6 50%,#a88466)" role="img" aria-label="Batter following through in front of a dugout with teammates"></div>

  <div class="abs photo" style="left:99px;top:1613px;background:linear-gradient(135deg,#6a3c22,#b07a4e 50%,#d3a77d)" role="img" aria-label="Yellow softball resting in a leather glove on the dirt"></div>
  <h3 class="abs row-title" style="left:633px;top:1655px">FALL CLASSIC</h3>
  <p class="abs row-copy" style="left:633px;top:1730px">Lorem ipsum dolor sit amet, consectetur adipiscing elit, sed do eiusmod tempor incididunt ut labore et dolore magna aliqua.</p>
  <div class="abs pill" style="left:633px;top:1834px">Read More</div>

  <svg class="abs about-bg" viewBox="0 0 1200 620" width="1200" height="620" aria-hidden="true">
    <polygon points="0,117 1200,7 1200,550 0,615" fill="#f5f5f5"/>
  </svg>
  <h2 class="abs row-title" style="left:101px;top:2092px;font-size:44px">ABOUT US</h2>
  <div class="abs rule" style="left:101px;top:2149px;width:145px"></div>
  <p class="abs about-copy">Lorem ipsum dolor sit amet, consectetur adipiscing elit, sed do eiusmod tempor incididunt ut labore et dolore magna aliqua. Ut enim ad minim veniam, quis nostrud exercitation ullamco laboris nisi ut aliquip ex ea commodo consequat. Lorem ipsum dolor sit amet, consectetur adipiscing elit, sed do eiusmod tempor incididunt ut labore et dolore magna aliqua. Ut enim ad minim veniam, quis nostrud exercitation ullamco laboris nisi ut aliquip ex ea commodo consequat.</p>
  <div class="abs pill" style="left:97px;top:2438px">Read More</div>
  <div class="abs about-mark"><span class="dot"></span>Kestrel<br>Softball</div>

  <h2 class="abs sec-title" style="top:2584px">HOW IT WORKS</h2>
  <div class="abs rule" style="left:479px;top:2651px;width:192px"></div>

  <div class="abs step" style="left:83px">
    <div class="badge"><svg width="54" height="54" viewBox="0 0 54 54" fill="none" stroke="#222" stroke-width="2.5"><rect x="6" y="10" width="36" height="34" rx="3"/><line x1="6" y1="19" x2="42" y2="19"/><line x1="14" y1="5" x2="14" y2="14"/><line x1="34" y1="5" x2="34" y2="14"/><circle cx="40" cy="40" r="9" fill="#f5ec1a"/><polyline points="40,35 40,40 44,42"/></svg></div>
    <h3>SCHEDULE</h3><p>At vero eos et accusamus</p>
  </div>
  <div class="abs step" style="left:291px">
    <div class="badge"><svg width="54" height="54" viewBox="0 0 54 54" fill="none" stroke="#222" stroke-width="2.5"><polyline points="4,10 11,10 17,36 43,36 48,18 14,18"/><circle cx="20" cy="44" r="3"/><circle cx="40" cy="44" r="3"/><circle cx="31" cy="15" r="9" fill="#f5ec1a"/><polyline points="27,15 30,18 35,12"/></svg></div>
    <h3>CHECKOUT</h3><p>At vero eos et accusamus</p>
  </div>
  <div class="abs step" style="left:499px">
    <div class="badge"><svg width="54" height="54" viewBox="0 0 54 54" fill="none" stroke="#222" stroke-width="2.5"><rect x="11" y="8" width="32" height="40" rx="3"/><rect x="20" y="4" width="14" height="7" rx="2"/><line x1="24" y1="20" x2="37" y2="20"/><line x1="24" y1="29" x2="37" y2="29"/><line x1="24" y1="38" x2="37" y2="38"/><line x1="16" y1="20" x2="19" y2="20"/><line x1="16" y1="29" x2="19" y2="29"/><line x1="16" y1="38" x2="19" y2="38"/></svg></div>
    <h3>ROSTER</h3><p>At vero eos et accusamus</p>
  </div>
  <div class="abs step" style="left:706px">
    <div class="badge"><svg width="58" height="58" viewBox="0 0 58 58" fill="none" stroke="#222" stroke-width="2.5"><rect x="14" y="4" width="30" height="9"/><text x="29" y="11.5" font-size="6.5" text-anchor="middle" fill="#222" stroke="none" font-family="Poppins,sans-serif">HOTEL</text><rect x="8" y="13" width="42" height="8"/><rect x="8" y="21" width="42" height="32"/><rect x="14" y="27" width="7" height="9"/><rect x="25" y="27" width="7" height="9"/><rect x="36" y="27" width="7" height="9"/><rect x="14" y="40" width="7" height="9"/><rect x="25" y="40" width="7" height="9"/><rect x="36" y="40" width="7" height="9"/></svg></div>
    <h3>HOTEL</h3><p>At vero eos et accusamus</p>
  </div>
  <div class="abs step" style="left:914px">
    <div class="badge"><svg width="54" height="54" viewBox="0 0 54 54" fill="none" stroke="#222" stroke-width="2.5"><circle cx="27" cy="27" r="20"/><polygon points="22,17 37,27 22,37"/></svg></div>
    <h3>PLAY</h3><p>At vero eos et accusamus</p>
  </div>

  <section aria-label="Contact form">
    <svg class="abs contact-bg" viewBox="0 0 1200 705" width="1200" height="705" role="img" aria-label="Dark navy toned photo of a fielder's glove on the field">
      <defs><linearGradient id="contactTone" x1="0" y1="0" x2="1" y2="1"><stop offset="0" stop-color="#1e2d4c"/><stop offset="0.5" stop-color="#2a3a4e"/><stop offset="1" stop-color="#1a2740"/></linearGradient></defs>
      <polygon points="0,85 1200,0 1200,640 0,700" fill="url(#contactTone)"/>
    </svg>
    <div class="abs contact-tag">CONTACT US</div>
    <div class="abs field" style="left:172px;top:3112px;width:427px;height:51px">Your Name</div>
    <div class="abs field" style="left:617px;top:3112px;width:403px;height:51px">Practice Name</div>
    <div class="abs field" style="left:172px;top:3197px;width:427px;height:51px">Email</div>
    <div class="abs field" style="left:617px;top:3197px;width:403px;height:51px">Phone Number</div>
    <div class="abs field" style="left:173px;top:3283px;width:423px;height:142px">Practice Specialty</div>
    <div class="abs field" style="left:619px;top:3283px;width:399px;height:142px">Any additional info you’d like to provide</div>
    <div class="abs submit">SUBMIT NOW</div>
  </section>
</main>

<footer>
  <div class="abs foot-brand">Kestrel<br>Softball</div>
  <nav>
    <span class="abs foot-nav" style="left:258px">Home</span>
    <span class="abs foot-nav" style="left:409px">About Us</span>
    <span class="abs foot-nav" style="left:569px">Benefits</span>
    <span class="abs foot-nav" style="left:733px">Programs</span>
    <span class="abs foot-nav" style="left:916px">Contact Us</span>
  </nav>
  <div class="abs foot-line"></div>
  <p class="abs copyright">Copyrights 2023 Kestrel Softball Tourney.All Rights Reserved</p>
</footer>

</body>
</html>
```